Stationery Design Project

KT7 Staffing requires letterhead and business card designs for a company based in London. Just like the name, we're a management resourcing company, providing resources to third party companies. You can see www.kt7staffing-example.com for ideas on existing colour schemes and design concepts that have been implimented and agreed to. Ultimately the design should broadcast professionalism, safety and the concept of growth.

Target Market(s)

Financial institutes; friendly societies (All UK based)

Industry/Entity Type

Safety

Requirements
Must have
• Files produced should be print ready; and the text in them editable (eg address, name etc)

```html
<!DOCTYPE html>
<html lang="en">
<head>
<meta charset="utf-8">
<title>KT7 Staffing – Business Card</title>
<link href="https://fonts.googleapis.com/css2?family=Arimo:ital,wght@0,400;0,700;1,400&display=swap" rel="stylesheet">
<style>
  :root {
    --page: #ffffff;
    --card-front: #7bbcd9;
    --card-back: #eef6fa;
    --brand-white: #ffffff;
    --sky: #7bbcd9;
    --teal: #0f8f9c;
    --ink: #1d3b4d;
    --rule: #b9d9e8;
  }
  * { margin: 0; padding: 0; box-sizing: border-box; }
  html, body {
    width: 1001px;
    height: 1200px;
    overflow: hidden;
    background: var(--page);
    font-family: "Arimo", Arial, sans-serif;
  }
  .canvas { position: relative; width: 1001px; height: 1200px; }

  .card {
    position: absolute;
    left: 50px;
    width: 890px;
    height: 508px;
  }
  .card-front { top: 68px; background: var(--card-front); }
  .card-back { top: 635px; background: var(--card-back); }

  .front-brand {
    position: absolute;
    inset: 0;
    display: flex;
    align-items: center;
    justify-content: center;
    gap: 28px;
  }
  .brand-dot {
    width: 46px; height: 46px;
    border-radius: 50%;
    background: var(--brand-white);
  }
  .brand-name {
    color: var(--brand-white);
    font-weight: 700;
    font-size: 84px;
    letter-spacing: 1px;
    line-height: 1;
  }

  .back-brand {
    position: absolute;
    left: 160px;
    width: 190px;
    top: 236px;
    text-align: right;
    color: var(--teal);
    font-weight: 700;
    font-size: 28px;
    line-height: 1;
    white-space: nowrap;
  }
  .divider {
    position: absolute;
    left: 380px;
    top: 190px;
    width: 2px;
    height: 275px;
    background: var(--rule);
  }
  .contact {
    position: absolute;
    left: 408px;
    top: 122px;
    font-size: 26px;
    line-height: 32.5px;
  }
  .contact-name { color: var(--sky); font-size: 28px; }
  .contact-role { color: var(--teal); font-style: italic; font-size: 27px; margin-bottom: 46px; }
  .contact-address { color: var(--sky); }
  .contact-detail { color: var(--ink); }
</style>
</head>
<body>
<div class="canvas">
  <section class="card card-front">
    <div class="front-brand">
      <span class="brand-dot"></span>
      <span class="brand-name">KT7 Staffing</span>
    </div>
  </section>

  <section class="card card-back">
    <div class="back-brand">KT7 Staffing</div>
    <div class="divider"></div>
    <div class="contact">
      <p class="contact-name">Oliver Hartley</p>
      <p class="contact-role">Consultant</p>
      <p class="contact-address">Harbour Point House,</p>
      <p class="contact-address">Kestrel Lane, London</p>
      <p class="contact-detail">0123 456 789</p>
      <p class="contact-detail">oliver@kt7staffing-example.com</p>
      <p class="contact-detail">www.kt7staffing-example.com</p>
    </div>
  </section>
</div>
</body>
</html>
```